Fresh pet feed direct from manufacturer to door step. Quality and Freshness un-surpassed in Industr

Need Business Card Design; leading into many other projects, for New Franchised Business Opportunity providing home delivery of fresh dog and cat feed (no emphasis needed for cat) direct from manufacturing facility. (no middle men or distributors) Food is Farm to Factory fresh. Our trademarked tagline is "Quality is our MAIN Ingredient ! "
Updates

Please take note of other contest for Chirplane Cover and Profile Pic's

Target Market(s)

Dog and Cat owners

Industry/Entity Type

Pet

Contact Information for Business Card

Name, address, local phone, national 800 number, website, email address

Other font styles liked:
• follow that from logo

Requirements
Must have
• Our feed is made in Texas with ingredients sourced from local farms. We want to lean heavy on the Made in West Texas , ranch theme but that has a 'black label', 'vantrel', 'premium', 'high-end' look and feel
Nice to have
• maybe have an offer on card? 20% off with promo code "x" etc.. ?? just a thought...

```html
<!DOCTYPE html>
<html lang="en">
<head>
<meta charset="utf-8">
<title>Marlow's Premium – Business Card</title>
<link href="https://fonts.googleapis.com/css2?family=Cinzel:wght@600&family=Arimo:wght@400&display=swap" rel="stylesheet">
<style>
  :root {
    --backdrop: #e6e2dc;
    --card: #f7f7f7;
    --card-shade: #e9e9e9;
    --ink: #1a1a1a;
    --plum: #241823;
    --gold: #c9a227;
    --band: #0d0d0d;
  }
  * { margin: 0; padding: 0; box-sizing: border-box; }
  html, body { width: 1200px; height: 885px; overflow: hidden; background: var(--backdrop); }
  .canvas {
    width: 1200px; height: 885px;
    display: flex; align-items: center; justify-content: center; gap: 90px;
  }
  .card {
    position: relative;
    width: 400px; height: 700px;
    background: linear-gradient(160deg, #ffffff 0%, var(--card) 55%, var(--card-shade) 100%);
    box-shadow: 0 6px 0 var(--band), 0 14px 30px rgba(0,0,0,.25);
    overflow: hidden;
  }
  .brand {
    display: flex; align-items: center; justify-content: center; gap: 14px;
    font-family: "Cinzel", serif; font-weight: 600; color: var(--plum);
    letter-spacing: 1px; line-height: 1.1; text-align: center;
  }
  .brand-dot { width: 26px; height: 26px; border-radius: 50%; background: var(--plum); flex: none; }
  .card-front .brand { position: absolute; inset: 0; font-size: 34px; }
  .card-back .brand { margin-top: 90px; font-size: 30px; }
  .holder-name {
    position: absolute; left: 52px; top: 400px;
    font-family: "Arimo", sans-serif; font-size: 24px; color: var(--gold);
  }
  .contact-list {
    position: absolute; left: 52px; top: 468px; list-style: none;
    font-family: "Arimo", sans-serif; font-size: 16px; color: var(--ink);
  }
  .contact-list li { display: flex; align-items: center; gap: 14px; height: 27px; }
  .contact-icon {
    width: 20px; height: 20px; background: var(--band);
    border: 1.5px solid var(--gold); border-radius: 3px;
    display: flex; align-items: center; justify-content: center; flex: none;
  }
  .bottom-band { position: absolute; left: 0; right: 0; bottom: 0; height: 70px; background: var(--band); }
</style>
</head>
<body>
<main class="canvas">
  <section class="card card-front">
    <div class="brand"><span class="brand-dot"></span><span>MARLOW'S<br>PREMIUM</span></div>
  </section>

  <section class="card card-back">
    <div class="brand"><span class="brand-dot"></span><span>MARLOW'S<br>PREMIUM</span></div>
    <p class="holder-name">Your Name</p>
    <ul class="contact-list">
      <li><span class="contact-icon"><svg width="12" height="12" viewBox="0 0 12 12"><path d="M2 1l2 0 1 3-1.5 1a7 7 0 0 0 3.5 3.5L8 7l3 1v2a1 1 0 0 1-1 1A9 9 0 0 1 1 2a1 1 0 0 1 1-1z" fill="#fff"/></svg></span>000 - 0000 000</li>
      <li><span class="contact-icon"><svg width="12" height="12" viewBox="0 0 12 12"><path d="M2 1l2 0 1 3-1.5 1a7 7 0 0 0 3.5 3.5L8 7l3 1v2a1 1 0 0 1-1 1A9 9 0 0 1 1 2a1 1 0 0 1 1-1z" fill="#fff"/></svg></span>000 - 0000 000</li>
      <li><span class="contact-icon"><svg width="12" height="12" viewBox="0 0 12 12"><circle cx="6" cy="6" r="5" fill="none" stroke="#fff" stroke-width="1.2"/><path d="M1 6h10M6 1c-3 3-3 7 0 10M6 1c3 3 3 7 0 10" fill="none" stroke="#fff" stroke-width="1"/></svg></span>www.marlows.com</li>
      <li><span class="contact-icon"><svg width="12" height="12" viewBox="0 0 12 12"><rect x="1" y="2.5" width="10" height="7" fill="none" stroke="#fff" stroke-width="1.2"/><path d="M1 2.5l5 4 5-4" fill="none" stroke="#fff" stroke-width="1.2"/></svg></span>name@marlows.com</li>
      <li><span class="contact-icon"><svg width="12" height="12" viewBox="0 0 12 12"><path d="M6 11C3 7 2.5 5.5 2.5 4.5a3.5 3.5 0 0 1 7 0C9.5 5.5 9 7 6 11z" fill="#fff"/><circle cx="6" cy="4.5" r="1.3" fill="#0d0d0d"/></svg></span>000 west, 1st street UA 00000</li>
    </ul>
    <div class="bottom-band"></div>
  </section>
</main>
</body>
</html>
```